ONE PAGE WEB DESIGN NEEDED for Finance Company

We need a web design (ONE PAGE DESIGN ONLY) for a new finance website called Brightwell Lending. Brightwell Lending helps customers get the right loan, whether its a home loan, investment loan, business loan etc.

You are required to come up with just the homepage design. Professionalism and quality is the key factors in the successful design.

Here are a few design questions to help you out:

-
What information should be used on the page?
Ive provided a document which outlines all the information needed to put on homepage (attached to the brief - called brightwell_page_info). Also see the Must Have section below on this brief.

-
What links should appear in the navigation/footer?:
The navigation should provide links to the following pages (NOTE: services link has subcategories):
1 Homepage
2 Services
- Home loans
- Investment loans
- Refinancing loans
- Business loans
3 About Us
4 FAQ
5 Contact Us

-
What colors should be used in the design?
Our company colors - Cyan: #2EADE3, Blue: #004B70, White. Feel free to submit designs with slight variations if you feel it improves the design.

-
What should the layout of the page be?
This is up to you to come up with - we are open to different layouts for the page design (as long as they capture the information effectively and making it easy to understand).

Target Market(s)

Potential Home owners, Families and Business Owners

Industry/Entity Type

Business

Requirements
Must have
• - Must contain our logo (attached as PNG and Illustrator file)
- Winning designer must supply a Photoshop file (PSD) that will allow us.
Nice to have
• - Should include photos/images of families, professional groups, tradespeople etc (you can use stock photos from PixQuarry and I will purchase them once you are selected as the winning design)
- Link to a loan calculator somewhere on front page with a button 'Find out how much you could borrow' (or maybe even try adding a loan calculator to the homepage if you think this would look good)
- Page should have a main headline "Finding the right loan for you" or "Brightwell Lending finds the right loan for our customers."
- Must include Accreditation logos somewhere on the homepage (will try and supply these soon)
Should not have
• - Poor quality designs will not be considered
- Do not use clipart

```html
<!DOCTYPE html>
<html lang="en">
<head>
<meta charset="utf-8">
<title>Brightwell Lending – Finding the right loan for you</title>
<link href="https://fonts.googleapis.com/css2?family=PT+Sans:ital,wght@0,400;0,700;1,400&family=Arimo:wght@400;700&family=Ubuntu:wght@500;700&display=swap" rel="stylesheet">
<style>
:root{
  --cyan:#2eade3;
  --blue:#004b70;
  --navy:#0d3f63;
  --sky:#5bc3ea;
  --text:#333;
  --muted:#666;
  --line:#dcdcdc;
  --footer:#2b2b2b;
  --footer-bar:#232323;
  --footer-text:#b9b9b9;
  --red:#c8102e;
}
*{margin:0;padding:0;box-sizing:border-box}
html,body{width:1078px;height:1200px;overflow:hidden;background:#fff}
body{position:relative;font-family:"Arimo",Arial,sans-serif;color:var(--text)}
.abs{position:absolute}

.hero-bg{left:0;top:0;width:1078px;height:580px;
  background:radial-gradient(ellipse at 40% 40%,#ffffff 0%,#eef4f9 55%,#e3ecf4 80%,#ffffff 100%)}
.hero-photo{left:144px;top:85px;width:388px;height:292px;border-radius:46% 46% 30% 30%;
  background:radial-gradient(ellipse at 50% 45%,#e7c3a8 0%,#d9b298 35%,#c9d6e2 70%,rgba(230,238,245,0) 100%)}

/* header */
.brand{left:153px;top:10px}
.brand-mark{left:47px;top:0;width:42px;height:42px;border-radius:50%;background:var(--cyan)}
.brand-name{left:0;top:47px;white-space:nowrap;font-family:"PT Sans",sans-serif;font-size:21px;font-weight:700;color:var(--cyan)}
.util{left:666px;top:23px;font-family:"PT Sans",sans-serif;font-style:italic;font-weight:700;font-size:10px;color:var(--navy)}
.util span{margin:0 5px;color:var(--cyan)}
.search{left:755px;top:17px;width:170px;height:23px;border:1px solid #cfd6dc;background:#fff}
.search input{border:0;width:140px;height:21px;padding-left:8px;font:italic 10px "PT Sans",sans-serif;color:#999;background:transparent}
.search-btn{position:absolute;right:-1px;top:-1px;width:26px;height:23px;background:var(--cyan)}
.nav{left:525px;top:58px;font-family:"PT Sans",sans-serif;font-size:15.5px;color:var(--cyan)}
.nav a{position:absolute;white-space:nowrap;text-decoration:none;color:var(--cyan)}
.nav a.active{color:var(--navy);font-weight:700}

/* bubble */
.bubble-text{left:612px;top:182px;color:#fff;font-family:"Ubuntu",sans-serif}
.bubble-text .l1{font-size:22px;font-weight:500}
.bubble-text .l2{font-size:36px;font-weight:700;line-height:34px;margin-top:-2px}
.bubble-text .l3{font-size:14px;font-weight:700;text-align:right;width:172px}

/* calculator */
.calc{left:228px;top:391px;width:622px;height:175px;background:#fff;border:1px solid #d5d9dd;border-radius:6px;box-shadow:0 1px 6px rgba(0,0,0,.12)}
.calc-label{font-family:"Ubuntu",sans-serif;font-weight:700;font-size:11px;color:var(--navy);white-space:nowrap}
.pill{display:inline-block;border:2px solid var(--navy);border-radius:50%;padding:2px 4px;color:var(--red);font-size:14px;margin:0 3px;background:#fff}
.calc-val{font-family:"Ubuntu",sans-serif;font-weight:700;font-size:11.5px;color:var(--navy);white-space:nowrap}
.val-box{border:1px solid #c9cdd1;border-radius:5px;font-family:"Ubuntu",sans-serif;font-weight:700;font-size:12px;color:var(--navy);display:flex;align-items:center;justify-content:center;box-shadow:inset 0 1px 2px rgba(0,0,0,.08)}
.total-label{left:270px;top:515px;font-family:"Ubuntu",sans-serif;font-weight:700;font-size:20px;letter-spacing:.5px;color:#fff}
.total-box{left:550px;top:512px;width:88px;height:31px;font-size:18px;font-weight:500;color:#333}
.apply-btn{left:721px;top:517px;width:84px;height:24px;border-radius:4px;background:linear-gradient(#1a7fb3,var(--blue));color:#fff;font-family:"Ubuntu",sans-serif;font-weight:700;font-size:10px;display:flex;align-items:center;justify-content:center;letter-spacing:.4px}

/* about */
.divider-v{left:674px;top:566px;width:1px;height:116px;background:linear-gradient(var(--line),rgba(220,220,220,0))}
h2.section{font-family:"Arimo",sans-serif;font-weight:400;font-size:20px;color:#444;white-space:nowrap}
.about-text{left:153px;top:615px;width:480px;font-size:9.8px;line-height:15px;letter-spacing:.3px;color:#444}
.about-text p+p{margin-top:15px}
.ghost-btn{border:1px solid #c6ccd1;border-radius:5px;background:linear-gradient(#fff,#eef1f3);color:var(--cyan);font:italic 10px "PT Sans",sans-serif;display:flex;align-items:center;justify-content:center}

.cash-title{left:717px;top:588px;font-size:17px;color:#444}
.cash-sub{left:717px;top:609px;font:italic 10.5px "PT Sans",sans-serif;color:var(--cyan)}
.field{left:716px;width:209px;height:22px;border:1px solid #d3d7db;border-radius:5px;background:#f1f2f3;font:italic 9px "PT Sans",sans-serif;color:#666;padding:6px 8px}

/* services */
.card{top:814px;width:176px}
.card-img{width:176px;height:116px}
.card h3{margin-top:22px;font-weight:400;font-size:14px;letter-spacing:.8px;color:#555}
.card p{margin-top:6px;font-size:9.8px;line-height:15px;letter-spacing:.3px;color:#444;text-align:justify}
.card .more{display:block;text-align:right;margin-top:3px;font-size:9.5px;color:var(--cyan)}
.arrow{top:870px}

/* footer */
.footer{left:0;top:1046px;width:1078px;height:124px;background:var(--footer)}
.footer-bar{left:0;top:1170px;width:1078px;height:30px;background:var(--footer-bar);border-top:1px solid #3a3a3a}
.fcol{top:1069px}
.fcol h4{font-weight:400;font-size:11.5px;color:#fff;white-space:nowrap;padding-bottom:6px;border-bottom:1px dotted #666}
.fcol ul{list-style:none;margin-top:6px}
.fcol li{font-size:9.8px;letter-spacing:.5px;color:var(--footer-text);line-height:15.6px;white-space:nowrap}
.fcol li::before{content:"";display:inline-block;border-left:4px solid #999;border-top:3px solid transparent;border-bottom:3px solid transparent;margin-right:7px}
.social li{line-height:19px}
.social li::before{display:none}
.social i{display:inline-block;width:13px;height:13px;border-radius:2px;background:#6d8fb8;vertical-align:-3px;margin-right:10px}
.testimonial{left:752px;top:1069px;width:173px}
.testimonial h4{font-weight:400;font-size:11.5px;color:#fff}
.testimonial blockquote{margin-top:9px;padding-left:15px;font-size:9.5px;line-height:11.5px;letter-spacing:.4px;color:#e0e0e0;position:relative}
.testimonial blockquote::before{content:"\201C";position:absolute;left:0;top:-4px;font-size:14px;color:#fff}
.testimonial cite{display:block;margin-top:6px;padding-left:15px;font-style:normal;font-size:9.5px;color:#fff}
.bottom-links{left:153px;top:1180px;font-size:10px;color:#fff;white-space:nowrap}
.bottom-links span{margin:0 6px;color:#888}
.copyright{right:153px;top:1180px;font-size:10px;color:#fff;white-space:nowrap}
</style>
</head>
<body>

<div class="abs hero-bg"></div>
<div class="abs hero-photo" role="img" aria-label="Photo of a smiling family of three hugging"></div>

<header>
  <div class="abs brand">
    <div class="abs brand-mark"></div>
    <div class="abs brand-name">Brightwell Lending</div>
  </div>
  <div class="abs util">Register<span>|</span>News</div>
  <div class="abs search">
    <input type="text" value="Search..." aria-label="Search">
    <div class="search-btn">
      <svg width="26" height="23" viewBox="0 0 26 23"><circle cx="12" cy="10.5" r="3.5" fill="none" stroke="#fff" stroke-width="1.5"/><line x1="14.5" y1="13" x2="17" y2="15.5" stroke="#fff" stroke-width="1.6"/></svg>
    </div>
  </div>
  <nav class="abs nav">
    <a class="active" style="left:0">Home</a>
    <a style="left:78px">Services</a>
    <a style="left:176px">About Us</a>
    <a style="left:270px">FAQ</a>
    <a style="left:329px">Contact Us</a>
  </nav>
</header>

<!-- headline bubbles -->
<svg class="abs" style="left:590px;top:110px" width="220" height="290" viewBox="590 110 220 290">
  <circle cx="699" cy="218" r="98" fill="var(--sky)"/>
  <circle cx="753" cy="342" r="38" fill="var(--sky)"/>
  <circle cx="706" cy="379" r="15" fill="var(--sky)"/>
</svg>
<h1 class="abs bubble-text">
  <div class="l1">finding the</div>
  <div class="l2">Right loan</div>
  <div class="l3">for you..</div>
</h1>

<!-- loan calculator -->
<section class="abs calc" aria-label="Loan calculator"></section>
<div class="abs calc-label" style="left:275px;top:412px">HOW MUCH<span class="pill">CASH</span>DO&nbsp; YOU WANT ?</div>
<div class="abs calc-val" style="left:503px;top:417px">$ 350</div>
<svg class="abs" style="left:548px;top:415px" width="108" height="14">
  <rect x="1" y="5" width="104" height="3" rx="1.5" fill="#d4d8dc"/>
  <rect x="1" y="5" width="54" height="3" rx="1.5" fill="var(--cyan)"/>
  <circle cx="55" cy="6.5" r="4.5" fill="#fff" stroke="#aaa"/><circle cx="55" cy="6.5" r="2" fill="var(--red)"/>
</svg>
<div class="abs calc-val" style="left:666px;top:417px">$ 1,000</div>
<div class="abs val-box" style="left:733px;top:409px;width:72px;height:26px">$ 500</div>
<div class="abs" style="left:259px;top:447px;width:560px;height:1px;background:var(--line)"></div>

<div class="abs calc-label" style="left:275px;top:467px">HOW<span class="pill">LONG</span>DO YOU WANT IT FOR ?</div>
<div class="abs calc-val" style="left:503px;top:473px">Days</div>
<svg class="abs" style="left:548px;top:471px" width="108" height="14">
  <rect x="1" y="5" width="104" height="3" rx="1.5" fill="#d4d8dc"/>
  <rect x="1" y="5" width="38" height="3" rx="1.5" fill="var(--cyan)"/>
  <circle cx="39" cy="6.5" r="4.5" fill="#fff" stroke="#aaa"/><circle cx="39" cy="6.5" r="2" fill="var(--red)"/>
</svg>
<div class="abs calc-val" style="left:696px;top:473px">30</div>
<div class="abs val-box" style="left:733px;top:464px;width:72px;height:26px">$&nbsp;&nbsp; 50</div>

<svg class="abs" style="left:226px;top:487px" width="266" height="72" viewBox="0 0 266 72">
  <defs><linearGradient id="repay" x1="0" y1="0" x2="0" y2="1"><stop offset="0" stop-color="#38b6e6"/><stop offset="1" stop-color="#0f7fb6"/></linearGradient></defs>
  <path d="M2 0 Q20 20 60 20 L208 20 L204 3 L264 36 L204 70 L208 54 L40 54 Q10 54 2 30 Z" fill="url(#repay)"/>
</svg>
<div class="abs total-label">TOTAL TO REPAY</div>
<div class="abs val-box total-box">$ 550</div>
<div class="abs apply-btn">APPLY NOW</div>

<!-- about -->
<div class="abs divider-v"></div>
<h2 class="abs section" style="left:153px;top:588px">About Us</h2>
<div class="abs about-text">
  <p>Lorem ipsum dolor sit amet, consectetuer adipiscing elit. Nam cursus. Morbi ut mi. Nullam enim leo, egestas id, condimentum at, laoreet mattis, massa. Sed eleifend nonummy diam. Praesent mauris ante, elementum et, bibendum at, posuere sit amet, nibh.</p>
  <p>Duis tincidunt lectus quis dui viverra vestibulum. Suspendisse vulputate aliquam dui. Nulla elementum dui ut augue. Aliquam vehicula mi at mauris.</p>
</div>
<div class="abs ghost-btn" style="left:154px;top:727px;width:90px;height:22px">Read More</div>

<!-- quick form -->
<h2 class="abs section cash-title">Get Cash Now!</h2>
<div class="abs cash-sub">Just fill Out the form</div>
<div class="abs field" style="top:637px">Enter Your First Name...</div>
<div class="abs field" style="top:674px">Enter Your Last Name...</div>
<div class="abs field" style="top:712px">Enter Your Email ID...</div>
<div class="abs ghost-btn" style="left:835px;top:759px;width:91px;height:21px">Apply Now</div>

<!-- services -->
<h2 class="abs section" style="left:153px;top:776px">Our Services</h2>
<svg class="abs arrow" style="left:126px" width="12" height="20"><polyline points="9,2 2,10 9,18" fill="none" stroke="#c5c5c5" stroke-width="2"/></svg>
<svg class="abs arrow" style="left:948px" width="12" height="20"><polyline points="3,2 10,10 3,18" fill="none" stroke="#c5c5c5" stroke-width="2"/></svg>

<article class="abs card" style="left:153px">
  <div class="card-img" role="img" aria-label="Photo of a family in front of their new house" style="background:linear-gradient(180deg,#6ea7dc 0%,#a9c9e6 45%,#c7705a 70%,#8a7a5a 100%)"></div>
  <h3>HOME LOANS</h3>
  <p>Lorem ipsum dolor sit amet, consecil tetuer adipiscing elit. Consectetuer adipiscing elit. Nam cursus.</p>
  <span class="more">» Learn more</span>
</article>
<article class="abs card" style="left:352px">
  <div class="card-img" role="img" aria-label="Photo of a couple saving money at home" style="background:linear-gradient(90deg,#f1ece6 0%,#d94a4f 35%,#e9e2d8 65%,#8b7b62 100%)"></div>
  <h3>INVESTMENT LOANS</h3>
  <p>Lorem ipsum dolor sit amet, consecil tetuer adipiscing elit. Consectetuer adipiscing elit. Nam cursus.</p>
  <span class="more">» Learn more</span>
</article>
<article class="abs card" style="left:551px">
  <div class="card-img" role="img" aria-label="Photo of a hand signing a loan application form" style="background:linear-gradient(135deg,#eef1f2 0%,#d8dee2 50%,#aeb7bf 100%)"></div>
  <h3>REFINANCING LOANS</h3>
  <p>Lorem ipsum dolor sit amet, consecil tetuer adipiscing elit. Consectetuer adipiscing elit. Nam cursus.</p>
  <span class="more">» Learn more</span>
</article>
<article class="abs card" style="left:751px">
  <div class="card-img" role="img" aria-label="Photo of business people shaking hands" style="background:linear-gradient(180deg,#9fb2c8 0%,#4c5d72 55%,#1f2a38 100%)"></div>
  <h3>BUSINESS LOANS</h3>
  <p>Lorem ipsum dolor sit amet, consecil tetuer adipiscing elit. Consectetuer adipiscing elit. Nam cursus.</p>
  <span class="more">» Learn more</span>
</article>

<!-- footer -->
<footer>
  <div class="abs footer"></div>
  <div class="abs fcol" style="left:153px;width:131px">
    <h4>Our Services</h4>
    <ul><li>Home Loans</li><li>Investment Loans</li><li>Refinancing Loans</li><li>Business Loans</li></ul>
  </div>
  <div class="abs fcol" style="left:323px;width:103px">
    <h4>About Us</h4>
    <ul><li>Blogs</li><li>Teams</li><li>Carrer</li></ul>
  </div>
  <div class="abs fcol" style="left:454px;width:114px">
    <h4>Help?</h4>
    <ul><li>Contact Us</li><li>Privacy Policy</li><li>Terms of Use</li></ul>
  </div>
  <div class="abs fcol social" style="left:600px;width:101px">
    <h4>Connect &amp; Share</h4>
    <ul><li><i></i>Friendloop</li><li><i></i>Chirpline</li><li><i></i>Workmesh</li><li><i style="background:#b84a4a"></i>Viewstream</li></ul>
  </div>
  <div class="abs testimonial">
    <h4>Testimonials</h4>
    <blockquote>Lorem ipsum dolor sit amet, consectetuer adipiscing elit. Nam cursus. Morbi ut mi. Nullam enim leo. ”</blockquote>
    <cite>Lorem Ipsum</cite>
  </div>
  <div class="abs footer-bar"></div>
  <div class="abs bottom-links">Home<span>|</span>Services<span>|</span>About Us<span>|</span>FAQ<span>|</span>Contact US</div>
  <div class="abs copyright">Copyright © 2012 Brightwell Lending - All rights reserved.</div>
</footer>

</body>
</html>
```